Township of Harlowden E-Alert Signup

Need to create print media that is designed for a Town in New Jersey that is starting a marketing campaign to get townspeople to sign up for the E-Alert system.Need print media that is 1. interchangeable in size (regular letter-size, as well as a poster size) 2. Branded with their colors, logo, etc. (green and white displayed in logo)3. Displays the incentives to sign up. Incentives:- Community Services/Announcements- Gov’t/Non-profit Resources- Tax Information- Employment opportunities- Municipal Services/Public Works/Recreation Divisions- Health Updates
Target Market(s)
Townspeople of Maplewood NJ
Industry/Entity Type
Government
Colors
Designer to choose colors to be used in the design.
Requirements
Must have
- 1. interchangeable in size (regular letter-size, as well as a poster size)
- 2. Branded with their colors, logo, etc. (green and white displayed in logo)
- 3. Displays the incentives to sign up.
- Incentives:
- - Community Services/Announcements
- - Gov’t/Non-profit Resources
- - Tax Information
- - Employment opportunities
- - Municipal Services/Public Works/Recreation Divisions
- - Health Updates

```html
<!DOCTYPE html>
<html lang="en">
<head>
<meta charset="utf-8">
<title>Town of Harlowden E-Alerts</title>
<link href="https://fonts.googleapis.com/css2?family=Gelasio:wght@400;500&display=swap" rel="stylesheet">
<style>
  :root {
    --green: #2a951c;
    --frame-green: #2f9a26;
    --ink: #111111;
    --paper: #ffffff;
    --street-light: #c9c2b4;
    --street-mid: #8a7b6a;
    --street-dark: #3e3a36;
  }
  * { margin: 0; padding: 0; box-sizing: border-box; }
  html, body { width: 777px; height: 1200px; overflow: hidden; background: var(--paper); }
  .poster {
    position: relative;
    width: 777px;
    height: 1200px;
    background: var(--paper);
    font-family: "Gelasio", Georgia, serif;
    color: var(--ink);
    overflow: hidden;
  }
  .street-scene {
    position: absolute;
    left: 0;
    top: 895px;
    width: 777px;
    height: 305px;
    background: linear-gradient(180deg, var(--paper) 0%, var(--street-light) 22%, var(--street-mid) 60%, var(--street-dark) 100%);
    clip-path: polygon(0 52%, 8% 48%, 20% 50%, 34% 34%, 50% 8%, 62% 20%, 70% 10%, 80% 0%, 92% 20%, 100% 22%, 100% 100%, 0 100%);
  }
  .frame {
    position: absolute;
    inset: 0;
    width: 777px;
    height: 1200px;
  }
  .seal {
    position: absolute;
    left: 463px;
    top: 45px;
    width: 270px;
    height: 268px;
    background: var(--paper);
    display: flex;
    align-items: center;
    justify-content: center;
  }
  .seal-ring {
    width: 260px;
    height: 260px;
    border: 3px solid var(--green);
    border-radius: 50%;
    display: flex;
    align-items: center;
    justify-content: center;
    text-align: center;
  }
  .seal-name {
    font-size: 26px;
    line-height: 1.25;
    color: var(--green);
    font-weight: 400;
  }
  .headline { position: absolute; left: 91px; top: 272px; color: var(--green); }
  .headline-town { font-size: 37px; line-height: 1.2; font-weight: 400; }
  .headline-title { font-size: 64px; line-height: 1.1; font-weight: 400; margin-top: 2px; }
  .signup-lead {
    position: absolute; left: 91px; top: 418px;
    font-size: 29px; font-weight: 400;
  }
  .benefits {
    position: absolute; left: 91px; top: 468px;
    list-style: none;
    font-size: 20px;
  }
  .benefits li { height: 44.2px; line-height: 24px; }
  .contact {
    position: absolute; left: 91px; top: 791px;
    font-size: 23px; color: var(--green);
  }
</style>
</head>
<body>
<main class="poster">
  <div class="street-scene" role="img" aria-label="Photograph of the downtown main street with Tudor-style shops, brick buildings and parked cars"></div>

  <svg class="frame" viewBox="0 0 777 1200" aria-hidden="true">
    <g fill="none" stroke="var(--frame-green)" stroke-width="2">
      <polyline points="529,36 36,36 36,1164 742,1164 742,247"/>
      <polyline points="463,53 54,53 54,1145 724,1145 724,314"/>
    </g>
  </svg>

  <div class="seal">
    <div class="seal-ring">
      <p class="seal-name">Township of<br>Harlowden</p>
    </div>
  </div>

  <header class="headline">
    <h2 class="headline-town">Town of Harlowden</h2>
    <h1 class="headline-title">E-Alerts</h1>
  </header>

  <p class="signup-lead">Sign up today for:</p>

  <ul class="benefits">
    <li>Community Services &amp; Announcements</li>
    <li>Government &amp; Non-Profit Resources</li>
    <li>Tax Information</li>
    <li>Employment Opportunities</li>
    <li>Municipal Services, Public Works, Recreation Divisions</li>
    <li>Health Updates</li>
  </ul>

  <p class="contact">Find out more at info@harlowden.com</p>
</main>
</body>
</html>
```